Pella Acupuncture Business Card Design

I would like a business card design for my acupuncture business which is based from 2 practices in Melbourne, Australia.

The front of the card should include:

*The Logo
* Name - Miranda Tovelisca (B.App.Sc.(TCM), Dip.Rem.Mass.). (I would like the letters after my name in slightly smaller font)
* Mobile number - 0472 318 604
* Web address - www.pellaacupuncture-example.com.au

On the back of the card I would somehow like to fit my 2 clinic addresses in. They are:

The Birchwood Restoration Rooms
842 Fennimore Rd, Camberwell VIC 3124
Ph: 1300 274 518

Quillbrook Integrative & Eastern Herbal Therapy Clinic
31 Marlowby Rd, Malvern East VIC 3145
Ph: (03) 9871 3352

If there is space, I'd also like to add to the back of the card - Next Appointment............................ (or something along those lines).

Thanks and happy designing!

Target Market(s)

Health consumers, and colleagues in the health industry

Industry/Entity Type

Clinic

Contact Information for Business Card

as above in brief

Requirements
Must have
• I've seen some ok designs coming in, however I'd like to avoid the generic look with the added curved line details etc. I don't particularly need extra patterns added to the card. I'd prefer it to look quite clean and simple, and using more earthy colours (I'm not super keen on the lime green that a lot of designs seem to include. I don't mind the full black or white look, (obviously the back side needs to be a lighter colour to allow me to write appointment details on it). I also quite like the idea of the background looking like brown recycled paper (just an idea - that's not 100% necessary).
Nice to have
• I have an idea that I could have the main flower part of the logo printed as metallic.
Should not have
• Generic patterns and too much added detail.

```html
<!DOCTYPE html>
<html lang="en">
<head>
<meta charset="utf-8">
<title>Pella Acupuncture – Business Card</title>
<link rel="stylesheet" href="https://fonts.googleapis.com/css2?family=Questrial&display=swap">
<style>
  :root {
    --backdrop: #6b5540;
    --ink: #1d1d1b;
    --band: #1b1b1a;
    --cream: #f5eed3;
    --sand: #e6d6a4;
    --gold: #cdb679;
    --olive: #a39a55;
    --emblem-light: #ece0b0;
    --emblem-mid: #c8b36e;
    --rule: #2a2a28;
  }
  * { box-sizing: border-box; margin: 0; padding: 0; }
  html, body {
    width: 1200px; height: 1023px; overflow: hidden;
    background: var(--backdrop);
    font-family: "Questrial", "Century Gothic", sans-serif;
    color: var(--ink);
  }
  .sheet {
    width: 1200px; height: 1023px;
    display: flex; flex-direction: column; align-items: center; justify-content: center; gap: 60px;
  }
  .card {
    position: relative; width: 700px; height: 400px; overflow: hidden;
    box-shadow: 0 6px 18px rgba(0,0,0,.35);
  }
  .card__band { position: absolute; top: 0; bottom: 0; width: 36px; background: var(--band); z-index: 2; }

  /* Emblem area: plain circle placeholder for the metallic flower mark */
  .emblem {
    position: absolute; border-radius: 50%;
    background: radial-gradient(circle, var(--emblem-light) 0%, var(--emblem-mid) 70%, var(--gold) 100%);
    box-shadow: 0 0 0 10px var(--band);
  }

  /* Back of card */
  .card--back { background: linear-gradient(120deg, var(--cream) 0%, var(--sand) 45%, var(--gold) 80%, var(--olive) 100%); }
  .card--back .card__band { right: 0; }
  .card--back .emblem { width: 320px; height: 320px; left: 380px; top: -120px; }
  .appointment { position: absolute; left: 40px; top: 36px; width: 270px; font-size: 20px; text-transform: uppercase; letter-spacing: .5px; }
  .appointment__row {
    display: flex; align-items: flex-end; gap: 10px;
    margin-top: 12px; margin-left: 26px; font-size: 17px; text-transform: none;
  }
  .appointment__line { flex: 1; border-bottom: 1.5px solid var(--rule); height: 18px; }
  .clinics { position: absolute; left: 66px; top: 214px; width: 330px; }
  .clinic { font-size: 15px; line-height: 1.3; margin-bottom: 14px; }

  /* Front of card */
  .card--front { background: linear-gradient(300deg, var(--cream) 0%, var(--sand) 45%, var(--gold) 80%, var(--olive) 100%); }
  .card--front .card__band { left: 0; }
  .card--front .emblem { width: 270px; height: 270px; left: 10px; top: 14px; }
  .brand {
    position: absolute; left: 70px; top: 74px; width: 150px; height: 150px; border-radius: 50%;
    background: var(--band); z-index: 3;
    display: flex; align-items: center; justify-content: center; text-align: center;
  }
  .brand__name { font-size: 17px; line-height: 1.25; letter-spacing: 1px; color: var(--cream); }
  .person { position: absolute; right: 40px; top: 205px; text-align: right; }
  .person__name { font-size: 36px; letter-spacing: .5px; }
  .person__credentials { font-size: 15px; margin-top: 6px; }
  .contact { position: absolute; left: 70px; bottom: 36px; font-size: 17px; }
  .contact__row { display: flex; align-items: center; gap: 12px; margin-top: 8px; }
  .contact__icon { width: 18px; height: 18px; }
</style>
</head>
<body>
<main class="sheet">
  <section class="card card--back" aria-label="Card back">
    <div class="emblem" role="img" aria-label="Metallic flower emblem area"></div>
    <div class="card__band"></div>
    <div class="appointment">
      Appointment:
      <div class="appointment__row">Date:<span class="appointment__line"></span></div>
      <div class="appointment__row">Time:<span class="appointment__line"></span></div>
    </div>
    <div class="clinics">
      <p class="clinic">The Birchwood Restoration Rooms<br>842 Fennimore Rd, Camberwell VIC 3124<br>P: 1300 274 518</p>
      <p class="clinic">Quillbrook Integrative &amp; Eastern Herbal<br>Therapy Clinic<br>31 Marlowby Rd, Malvern East VIC 3145<br>P: (03) 9871 3352</p>
    </div>
  </section>

  <section class="card card--front" aria-label="Card front">
    <div class="emblem" role="img" aria-label="Metallic flower emblem area"></div>
    <div class="card__band"></div>
    <div class="brand"><span class="brand__name">Pella<br>Acupuncture</span></div>
    <div class="person">
      <p class="person__name">Miranda Tovelisca</p>
      <p class="person__credentials">B.App.Sc.(TCM), Dip.Rem.Mass.</p>
    </div>
    <div class="contact">
      <div class="contact__row">
        <svg class="contact__icon" viewBox="0 0 20 20" aria-hidden="true">
          <rect x="5" y="1.5" width="10" height="17" rx="2" fill="none" stroke="#1d1d1b" stroke-width="1.6"/>
          <line x1="8.5" y1="15.5" x2="11.5" y2="15.5" stroke="#1d1d1b" stroke-width="1.6"/>
        </svg>
        <span>0472 318 604</span>
      </div>
      <div class="contact__row">
        <svg class="contact__icon" viewBox="0 0 20 20" aria-hidden="true">
          <circle cx="10" cy="10" r="8.5" fill="none" stroke="#1d1d1b" stroke-width="1.6"/>
          <ellipse cx="10" cy="10" rx="3.6" ry="8.5" fill="none" stroke="#1d1d1b" stroke-width="1.3"/>
          <line x1="1.5" y1="10" x2="18.5" y2="10" stroke="#1d1d1b" stroke-width="1.3"/>
        </svg>
        <span>www.pellaacupuncture-example.com.au</span>
      </div>
    </div>
  </section>
</main>
</body>
</html>
```